Post it Note design

POST-IT NOTE DESIGN (CONTENT)
Size recommended: 4x6 for handwriting space.
Header (Bold):
Lighting Issue Detected on Your Property
Sub-header:
During our routine night inspection, we noted the following item(s):
Checkbox List:
⬜ Building Lights Out
⬜ Pole Lights Out
⬜ Sign Not Illuminated
⬜ Other ________________________
Action Line:
We can provide a quote or dispatch service right away.
Area for notes
Contact Block (Bold & Centered):
Brovane Fixture Inc.
Service@BrovaneFixture.com
www.BrovaneFixture.com
877-514-0862
Industry/Entity Type
Electrical lighting
Colors
Designer to choose colors to be used in the design.
Look and feel
Each slider illustrates characteristics of the customer's brand and the style your logo design should communicate.

```html
<!DOCTYPE html>
<html lang="en">
<head>
<meta charset="utf-8">
<title>Brovane Fixture Inc. – Lighting Issue Note</title>
<link rel="stylesheet" href="https://fonts.googleapis.com/css2?family=Anton&family=Quicksand:wght@500;600;700&family=Montserrat:wght@600;800&display=swap">
<style>
  :root {
    --navy: #1f2f8f;
    --navy-dark: #17237a;
    --red: #e10f1a;
    --paper: #ffffff;
    --backdrop: #d9d9d9;
    --notes-grey: #c9c9c9;
    --photo-steel: #b9bec6;
    --photo-truck: #e7e9ec;
  }
  * { box-sizing: border-box; margin: 0; padding: 0; }
  html, body { width: 1200px; height: 1200px; overflow: hidden; }
  body { background: var(--backdrop); position: relative; font-family: "Quicksand", sans-serif; }

  .note {
    position: absolute; left: 220px; top: 30px;
    width: 760px; height: 1140px;
    background: var(--paper);
    box-shadow: 0 6px 24px rgba(0,0,0,.18);
    overflow: hidden;
  }

  .note-title {
    position: absolute; top: 58px; left: 0; width: 100%;
    text-align: center;
    font-family: "Anton", sans-serif;
    font-size: 70px; line-height: 1;
    color: var(--navy); text-transform: uppercase; letter-spacing: .5px;
  }
  .note-intro {
    position: absolute; top: 236px; left: 0; width: 100%;
    text-align: center;
    font-size: 31px; font-weight: 600; line-height: 1.25;
    color: var(--red);
  }

  .checklist { position: absolute; top: 365px; left: 70px; width: 640px; list-style: none; }
  .checklist li {
    display: flex; align-items: center; height: 56px;
    font-size: 29px; font-weight: 600; color: var(--navy);
  }
  .checkbox { width: 30px; height: 30px; border: 3px solid var(--navy); margin-right: 22px; flex: none; }
  .fill-line { flex: 1; border-bottom: 2.5px solid var(--navy); margin-left: 16px; height: 26px; }

  .action-band {
    position: absolute; top: 622px; left: 0; width: 100%; height: 110px;
    background: var(--red);
    display: flex; align-items: center; justify-content: center;
    text-align: center;
    font-family: "Montserrat", sans-serif; font-weight: 800;
    font-size: 28px; line-height: 1.2; color: #fff; text-transform: uppercase;
  }

  .notes-box {
    position: absolute; top: 758px; left: 40px; width: 680px; height: 140px;
    border: 3px dotted var(--navy); border-radius: 14px;
  }
  .notes-label {
    position: absolute; left: 14px; top: 50%;
    transform: translateY(-50%) rotate(-90deg); transform-origin: left center;
    margin-left: 24px; margin-top: 60px;
    font-family: "Montserrat", sans-serif; font-weight: 600;
    font-size: 32px; letter-spacing: 2px; color: var(--notes-grey);
  }

  .photo-fixtures {
    position: absolute; left: 30px; top: 912px; width: 210px; height: 148px;
    background: linear-gradient(160deg, #dfe3e8 0%, var(--photo-steel) 55%, #8a8f98 100%);
    border-radius: 6px;
  }
  .photo-truck {
    position: absolute; right: 24px; top: 900px; width: 230px; height: 150px;
    background: linear-gradient(180deg, #f4f5f7 0%, var(--photo-truck) 60%, #c8ccd2 100%);
    border-radius: 6px;
  }

  .brand-name {
    position: absolute; left: 258px; top: 940px; width: 240px;
    text-align: center;
    font-family: "Montserrat", sans-serif; font-weight: 800;
    font-size: 31px; line-height: 1.1; color: var(--red);
  }

  .contact-bar { position: absolute; left: 0; bottom: 0; width: 100%; height: 80px; display: flex; }
  .contact-phone {
    width: 52%; background: var(--red); color: #fff;
    display: flex; align-items: center; justify-content: center; gap: 12px;
    font-family: "Montserrat", sans-serif; font-weight: 800; font-size: 38px;
  }
  .contact-online {
    flex: 1; background: var(--navy-dark); color: #fff;
    display: flex; flex-direction: column; justify-content: center; gap: 4px;
    padding-left: 20px;
    font-size: 17px; font-weight: 600;
  }
  .contact-online span { display: flex; align-items: center; gap: 8px; }
  .icon { flex: none; }
</style>
</head>
<body>
  <main class="note">
    <h1 class="note-title">Lighting Issue Detected<br>On Your Property</h1>
    <p class="note-intro">During our routine night inspection,<br>we noted the following item(s):</p>

    <ul class="checklist">
      <li><span class="checkbox"></span>Building Lights Out</li>
      <li><span class="checkbox"></span>Pole Lights Out</li>
      <li><span class="checkbox"></span>Sign Not Illuminated</li>
      <li><span class="checkbox"></span>Other<span class="fill-line"></span></li>
    </ul>

    <div class="action-band">We can provide a quote or dispatch<br>service right away.</div>

    <div class="notes-box"><span class="notes-label">NOTES</span></div>

    <div class="photo-fixtures" role="img" aria-label="Photo of a technician servicing pole-mounted parking lot light fixtures"></div>
    <div class="brand-name">Brovane Fixture Inc.</div>
    <div class="photo-truck" role="img" aria-label="Photo of a white bucket truck with safety cones"></div>

    <footer class="contact-bar">
      <div class="contact-phone">
        <svg class="icon" width="30" height="30" viewBox="0 0 24 24" aria-hidden="true"><path fill="#fff" d="M6.6 10.8c1.4 2.8 3.8 5.1 6.6 6.6l2.2-2.2c.3-.3.7-.4 1-.2 1.1.4 2.3.6 3.6.6.6 0 1 .4 1 1V20c0 .6-.4 1-1 1C10.6 21 3 13.4 3 4c0-.6.4-1 1-1h3.5c.6 0 1 .4 1 1 0 1.3.2 2.5.6 3.6.1.3 0 .7-.2 1l-2.3 2.2z"/></svg>
        877-514-0862
      </div>
      <div class="contact-online">
        <span><svg class="icon" width="16" height="12" viewBox="0 0 16 12" aria-hidden="true"><rect x="0.5" y="0.5" width="15" height="11" fill="#fff"/><path d="M1 1l7 6 7-6" stroke="#17237a" stroke-width="1.4" fill="none"/></svg>Service@BrovaneFixture.com</span>
        <span><svg class="icon" width="16" height="16" viewBox="0 0 16 16" aria-hidden="true"><circle cx="8" cy="8" r="7" stroke="#fff" stroke-width="1.4" fill="none"/><ellipse cx="8" cy="8" rx="3" ry="7" stroke="#fff" stroke-width="1.2" fill="none"/><path d="M1 8h14" stroke="#fff" stroke-width="1.2"/></svg>www.BrovaneFixture.com</span>
      </div>
    </footer>
  </main>
</body>
</html>
```